Business Card design for construction company

I would like a business card design for a construction company - Harlow Constructions. I have attached the ai logo file for use. I would like the card to be very smart and clean and incorporate only white and the two colours in the logo. I would like the card to have two sides. One side can just have the logo, the other with the relevant information.

Target Market(s)

Building and Construction Clients

Industry/Entity Type

Business

Contact Information for Business Card

Name: Tom Pardoe
Company: Harlow Constructions Pty Limited
Address: 14 Mallee Crescent Carrow Vale 2093
Phone: 0427 531 068
Email: tomp@harlowbuild-example.com.au

Font styles to use
Serif
Sans Serif

Requirements
Must have
• Details noted above
• Logo as provided
• Colours as in logo
• Square edges
• A font that compliments the logo
Should not have
• Any colour other than white and those in logo
• Rounded edges

```html
<!DOCTYPE html>
<html lang="en">
<head>
<meta charset="utf-8">
<title>Harlow Constructions – Business Card</title>
<link rel="stylesheet" href="https://fonts.googleapis.com/css2?family=Roboto:wght@400;500;700&display=swap">
<style>
  :root {
    --brand-blue: #1787d2;
    --brand-blue-light: #2595de;
    --brand-blue-dark: #0b78c2;
    --charcoal: #3c3c3e;
    --paper: #f2f2f2;
    --white: #ffffff;
    --backdrop: #c4c4c4;
  }
  * { margin: 0; padding: 0; box-sizing: border-box; }
  html, body {
    width: 1200px; height: 576px; overflow: hidden;
    background: var(--backdrop);
    font-family: "Roboto", Arial, sans-serif;
  }
  .stage { position: relative; width: 1200px; height: 576px; }
  .card {
    position: absolute; width: 482px; height: 292px; overflow: hidden;
    box-shadow: 0 3px 6px rgba(0,0,0,.25);
  }
  .card--front {
    left: 82px; top: 139px;
    background: linear-gradient(180deg, var(--brand-blue-dark) 0%, var(--brand-blue-light) 100%);
  }
  .card--back { left: 602px; top: 138px; background: var(--brand-blue); }

  .wordmark {
    position: absolute; left: 0; right: 0; top: 128px;
    text-align: center; color: var(--white);
    font-size: 27px; font-weight: 400; letter-spacing: 3px; text-transform: uppercase;
  }
  .web-line {
    position: absolute; left: 0; right: 0; bottom: 21px;
    display: flex; align-items: center; justify-content: center; gap: 16px;
    color: var(--white); font-size: 13px;
  }
  .rule { width: 68px; height: 2px; background: rgba(255,255,255,.85); }

  .back-shape { position: absolute; inset: 0; }
  .back-wordmark {
    position: absolute; left: 0; right: 0; top: 54px;
    text-align: center; color: var(--charcoal);
    font-size: 25px; font-weight: 400; letter-spacing: 3px; text-transform: uppercase;
  }
  .person {
    position: absolute; left: 56px; top: 162px; width: 150px; text-align: right; color: var(--white);
  }
  .person__name { font-size: 19px; font-weight: 700; letter-spacing: 1px; text-transform: uppercase; }
  .person__role { font-size: 12px; margin-top: 5px; }
  .divider { position: absolute; left: 216px; top: 152px; width: 1px; height: 60px; background: rgba(255,255,255,.8); }
  .contacts { position: absolute; left: 232px; top: 161px; color: var(--white); font-size: 13px; }
  .contacts li { list-style: none; display: flex; align-items: center; gap: 9px; height: 19px; }
  .contacts svg { width: 12px; height: 12px; fill: var(--white); }
  .company {
    position: absolute; left: 0; right: 0; top: 229px; text-align: center;
    color: var(--white); font-size: 13px; font-weight: 700;
  }
  .address {
    position: absolute; left: 0; right: 0; top: 253px;
    display: flex; align-items: center; justify-content: center; gap: 22px;
    color: var(--white); font-size: 13px;
  }
</style>
</head>
<body>
<main class="stage">
  <section class="card card--front">
    <p class="wordmark">Harlow Constructions</p>
    <p class="web-line"><span class="rule"></span>www.harlowbuild-example.com.au<span class="rule"></span></p>
  </section>

  <section class="card card--back">
    <svg class="back-shape" viewBox="0 0 482 292" preserveAspectRatio="none" aria-hidden="true">
      <path d="M0 0 H482 V98 Q240 150 0 92 Z" fill="var(--paper)"/>
      <path d="M0 92 Q240 150 482 98 V107 Q250 162 0 96 Z" fill="var(--charcoal)"/>
    </svg>
    <p class="back-wordmark">Harlow Constructions</p>

    <div class="person">
      <p class="person__name">Tom Pardoe</p>
      <p class="person__role">Managing Director</p>
    </div>
    <span class="divider"></span>
    <ul class="contacts">
      <li>
        <svg viewBox="0 0 24 24"><path d="M3 8c0-3 4-5 9-5s9 2 9 5v2h-5V8H8v2H3zM6 11h12l3 9H3z"/></svg>
        0427 531 068
      </li>
      <li>
        <svg viewBox="0 0 24 24"><path d="M2 5h20v14H2zM4 7v1l8 5 8-5V7l-8 5z"/></svg>
        tomp@harlowbuild-example.com.au
      </li>
    </ul>

    <p class="company">Harlow Constructions Pty Limited</p>
    <p class="address"><span class="rule"></span>14 Mallee Crescent Carrow Vale 2093<span class="rule"></span></p>
  </section>
</main>
</body>
</html>
```